Counseling Design Website

My husband and I are both counselors and have a business called K & J counseling. We have already purchased a logo from you in October of 2022. We both have expertise in Autism, Dyslexia, ADHD, Couples Counseling, Marriage and Family counseling, and Geriatrics. I would also like to have my forms online. I am planning on using Google sites. I have started a site, but havent gotten very far. I would like to have it created where i can just copy and paste so to speak.
https://pages.brindlehost.net/d/7kQzLp2Xv8T-NR_cY4wHaEm31PBUFsRdk/p/3HXyPq5WmA9bsjtd2EsLZFhRwGGKvTnYA/edit

```html
<!DOCTYPE html>
<html lang="en">
<head>
<meta charset="utf-8">
<title>K &amp; J Counseling</title>
<link rel="stylesheet" href="https://fonts.googleapis.com/css2?family=Poppins:wght@300;400;500;600;700&family=Lato:wght@400;700&family=Lora:wght@400&family=Roboto+Condensed:wght@700&family=Roboto:wght@400&display=swap">
<style>
:root{
  --purple:#7c4dff;
  --purple-dark:#6a3cf0;
  --green:#5cb93b;
  --ink:#333333;
  --text:#444444;
  --muted:#555555;
  --header-bg:#f7f7f7;
  --wave:#d8ecfb;
  --wave-deep:#cfe6f8;
  --footer-bg:#333333;
  --lilac:#f2edf9;
  --ice:#f2f8fd;
  --field:#f7f7f7;
  --field-line:#e4e4e4;
  --alert:#e0605a;
}
*{margin:0;padding:0;box-sizing:border-box}
html,body{width:1200px;height:3087px;overflow:hidden}
body{position:relative;background:#fff;font-family:'Lato',sans-serif;color:var(--text)}
.abs{position:absolute}
section,header,footer{position:absolute;left:0;width:1200px}

/* header */
.site-header{top:0;height:90px;background:var(--header-bg)}
.call-box{left:0;top:0;width:185px;height:90px;background:var(--purple);color:#fff;font-family:'Poppins',sans-serif;padding:28px 0 0 26px}
.call-box .label{font-size:15px;line-height:18px}
.call-box .number{font-size:19px;line-height:24px;font-weight:500}
.call-badge{left:162px;top:22px;width:48px;height:48px;border-radius:50%;background:#fff;border:3px solid var(--purple);display:flex;align-items:center;justify-content:center}
.book-btn{left:246px;top:29px;width:175px;height:36px;border:2px solid var(--green);border-radius:3px;color:var(--green);font-family:'Poppins',sans-serif;font-size:14px;font-weight:500;display:flex;align-items:center;justify-content:center}
.brand-top{left:520px;top:30px;width:160px;text-align:center;font-family:'Poppins',sans-serif;font-size:16px;font-weight:500;color:var(--purple)}
.main-nav{top:37px;font-family:'Poppins',sans-serif;font-size:15px;font-weight:500;color:var(--ink)}
.main-nav.active{color:var(--purple)}

/* hero */
.hero{top:90px;height:647px;overflow:hidden}
.hero-brand{left:150px;top:300px;width:460px;text-align:center;font-family:'Poppins',sans-serif;font-size:46px;font-weight:600;color:var(--purple)}
.hero-waves{left:0;top:470px}
.hero-welcome{left:650px;top:112px;font-family:'Poppins',sans-serif;font-size:37px;font-weight:400;color:var(--ink);letter-spacing:.5px}
.hero-title{left:649px;top:156px;font-family:'Poppins',sans-serif;font-size:43px;font-weight:600;color:var(--purple)}
.hero-copy{left:650px;top:224px;width:430px;font-size:20.5px;line-height:30px;color:var(--ink)}
.btn{display:flex;align-items:center;justify-content:center;color:#fff;font-family:'Roboto Condensed',sans-serif;font-weight:700;font-size:14px;border-radius:3px;box-shadow:0 6px 10px rgba(0,0,0,.18)}
.btn-purple{background:var(--purple)}
.btn-green{background:var(--green)}
.dots{left:562px;top:547px;display:flex;gap:8px;align-items:center}
.dots span{width:8px;height:8px;border-radius:50%;background:#fff}
.dots span.on{width:13px;height:13px}

/* faint side lettering */
.side-word{left:-195px;top:627px;width:470px;transform:rotate(-90deg);font-family:'Poppins',sans-serif;font-weight:700;font-size:92px;color:rgba(0,0,0,.045);letter-spacing:2px;white-space:nowrap;text-align:center;z-index:2}

/* about */
.about{top:737px;height:626px}
.about-photo{left:84px;top:54px;width:530px;height:494px;background:linear-gradient(135deg,#b7c8d6,#8fa0ad 45%,#c9b49c 80%,#e6e0d8)}
.about-strip{left:84px;top:548px;width:530px;height:12px;background:#eaf7ea}
.eyebrow{font-family:'Lora',serif;color:var(--purple);font-size:26px}
.section-title{font-family:'Poppins',sans-serif;font-weight:700;color:#111;letter-spacing:.3px}
.about .eyebrow{left:673px;top:100px}
.about .section-title{left:673px;top:144px;font-size:34px}
.about-copy{left:673px;top:203px;width:432px;font-size:15.6px;line-height:23.2px;color:var(--ink)}

/* services */
.services{top:1363px;height:845px;background:linear-gradient(122deg,var(--lilac) 0 43%,var(--ice) 43% 100%)}
.services .eyebrow{left:96px;top:256px;font-size:22px}
.services .section-title{left:96px;top:287px;font-size:27px;color:var(--ink)}
.rule{height:3px;background:var(--purple)}
.services-copy{left:96px;top:358px;width:242px;font-size:15.6px;line-height:23.3px;color:var(--ink)}
.card{width:227px;height:332px;background:#fff;box-shadow:0 2px 10px rgba(0,0,0,.06);text-align:center;padding-top:50px}
.card svg{display:block;margin:0 auto}
.card h3{font-family:'Poppins',sans-serif;font-size:17px;font-weight:600;color:var(--ink);margin-top:28px;letter-spacing:.3px}
.card p{font-size:13.2px;line-height:19px;color:var(--muted);width:180px;margin:14px auto 0}
.card.featured{background:linear-gradient(160deg,#7e55ff,#6b40f4);color:#fff;padding-top:38px}
.card.featured h3{color:#fff;line-height:25px;margin-top:14px}
.card.featured p{color:#fff;margin-top:8px}

/* chat */
.chat{top:2208px;height:559px}
.chat-photo{left:0;top:0;width:632px;height:559px;background:linear-gradient(180deg,#d8d2c8,#bdb3a6 55%,#8b8077)}
.chat-title{left:690px;top:50px;font-family:'Poppins',sans-serif;font-size:24px;font-weight:700;color:#111}
.chat-copy{left:691px;top:119px;width:370px;font-size:14.8px;line-height:21px;color:var(--ink)}
.field{height:44px;background:var(--field);border:1px solid var(--field-line);font-family:'Roboto',sans-serif;font-size:11.5px;color:#555;padding:0 17px;display:flex;align-items:center}
.field.focus{background:#fff;border:1.5px solid var(--alert);color:var(--alert)}
.field.area{height:71px;align-items:flex-start;padding-top:16px}

/* footer */
.site-footer{top:2767px;height:320px;background:var(--footer-bg);color:#fff}
.foot-title{left:155px;top:66px;font-family:'Poppins',sans-serif;font-size:26px;font-weight:300;letter-spacing:.5px}
.foot-rule{left:155px;top:120px;width:67px;height:2px;background:var(--purple)}
.hq{left:155px;top:158px;font-size:13.5px;letter-spacing:.3px}
.hq-addr{left:156px;top:188px;font-size:12.5px;line-height:22px}
.ico{width:38px;height:38px;border-radius:50%;background:var(--purple);display:flex;align-items:center;justify-content:center}
.contact-line{left:395px;font-size:14px;line-height:18px}
.contact-line strong{display:block;font-weight:400;font-size:17px;line-height:26px}
.foot-divider{left:659px;top:52px;width:1px;height:268px;background:#474747}
.brand-foot{left:733px;top:72px;font-family:'Lato',sans-serif;font-size:19px;font-weight:700;color:#fff}
.foot-links{left:730px;top:195px;font-size:16px}
.foot-links span{margin:0 14px}
.copyright{left:729px;top:238px;font-size:16px}
</style>
</head>
<body>

<header class="site-header">
  <div class="abs call-box"><div class="label">Call us at</div><div class="number">1.888.888.888</div></div>
  <div class="abs call-badge">
    <svg width="24" height="24" viewBox="0 0 24 24"><path d="M6.6 10.8c1.4 2.8 3.8 5.1 6.6 6.6l2.2-2.2c.3-.3.7-.4 1-.2 1.1.4 2.3.6 3.6.6.6 0 1 .4 1 1V20c0 .6-.4 1-1 1C10.6 21 3 13.4 3 4c0-.6.4-1 1-1h3.5c.6 0 1 .4 1 1 0 1.3.2 2.5.6 3.6.1.3 0 .7-.2 1z" fill="none" stroke="#7c4dff" stroke-width="1.6"/></svg>
  </div>
  <div class="abs book-btn">Book An Appointment</div>
  <div class="abs brand-top">K &amp; J Counseling</div>
  <nav>
    <div class="abs main-nav active" style="left:759px">Home</div>
    <div class="abs main-nav" style="left:836px">About us</div>
    <div class="abs main-nav" style="left:935px">Services</div>
    <div class="abs main-nav" style="left:1030px">Contact us</div>
  </nav>
</header>

<section class="hero">
  <svg class="abs hero-waves" width="1200" height="177" viewBox="0 0 1200 177">
    <path d="M0 62 C80 40 150 55 230 72 C330 92 420 62 520 48 C610 36 690 70 780 66 C880 62 960 30 1050 42 C1120 52 1160 66 1200 60 V177 H0Z" fill="#e6f3fd"/>
    <path d="M0 82 C100 68 170 78 260 92 C360 106 450 80 560 72 C660 66 740 98 840 90 C940 82 1020 60 1110 70 C1150 74 1180 82 1200 80 V177 H0Z" fill="var(--wave)"/>
    <path d="M0 118 C120 104 240 120 380 114 C520 108 640 124 780 118 C920 112 1060 100 1200 108 V177 H0Z" fill="var(--wave-deep)"/>
  </svg>
  <div class="abs hero-brand">K &amp; J Counseling</div>
  <div class="abs dots"><span></span><span></span><span class="on"></span><span></span><span></span></div>
  <div class="abs hero-welcome">WELCOME TO</div>
  <h1 class="abs hero-title">K &amp; J COUNSELING</h1>
  <p class="abs hero-copy">Lorem Ipsum is simply dummy text of the printing and typesetting industry. Lorem Ipsum has been the industry's standard dummy text ever since the 1500s, type specimen book.</p>
  <div class="abs btn btn-purple" style="left:643px;top:369px;width:155px;height:40px">LEARN MORE</div>
  <div class="abs btn btn-green" style="left:807px;top:369px;width:155px;height:40px">GET STARTED</div>
</section>

<div class="abs side-word">ABOUT US</div>

<section class="about">
  <div class="abs about-photo" role="img" aria-label="Counselor taking notes during a group session with three clients on a sofa"></div>
  <div class="abs about-strip"></div>
  <div class="abs eyebrow">K &amp; J Counseling</div>
  <h2 class="abs section-title">ABOUT US</h2>
  <p class="abs about-copy">Lorem Ipsum is simply dummy text of the printing and typesetting industry. Lorem Ipsum has been the industry's standard dummy text ever since the 1500s, when an unknown printer took a galley of type and scrambled it to make a type specimen book. It has survived not only five centuries, but also the leap into electronic typesetting, remaining essentially unchanged. It was popularised in the 1960s with the release of Letraset sheets containing Lorem Ipsum passages, and more recently with desktop publishing software like Aldus PageMaker including versions of Lorem Ipsum</p>
  <div class="abs btn btn-purple" style="left:673px;top:451px;width:109px;height:41px">READ MORE</div>
</section>

<section class="services">
  <div class="abs eyebrow">Service offering</div>
  <h2 class="abs section-title">WHAT WE DO</h2>
  <div class="abs rule" style="left:96px;top:337px;width:70px"></div>
  <p class="abs services-copy">Sed ut perspiciatis unde omnis iste natus error sit voluptatem accusantium doloremque laudantium, totam rem aperiam, eaque ipsa quae ab illo inventore veritatis et quasi architecto beatae vitae dicta sunt explicabo. Nemo enim ipsam</p>
  <div class="abs btn btn-purple" style="left:96px;top:548px;width:214px;height:37px;font-size:12.5px">VIEW MORE SERVICE OFFERING</div>

  <div class="abs card" style="left:372px;top:73px">
    <svg width="80" height="84" viewBox="0 0 80 84" fill="none" stroke="#7c4dff" stroke-width="2.4" stroke-linejoin="round"><path d="M24 80V64C14 58 9 48 9 37 9 19 22 6 40 6s31 12 31 28c0 4-1 7 2 12l-5 3v9c0 4-3 7-7 7h-6v15"/><path d="M30 24h10v-4a3 3 0 016 0v4h10v10h-4a3 3 0 000 6h4v10H30z"/></svg>
    <h3>AUTISM</h3>
    <p>Lorem Ipsum is simply dummy text of the printing and typesetting industry. Lorem Ipsum has been the industry's standard dummy</p>
  </div>
  <div class="abs card" style="left:623px;top:73px">
    <svg width="80" height="84" viewBox="0 0 80 84" fill="none" stroke="#7c4dff" stroke-width="2.4" stroke-linejoin="round" stroke-linecap="round"><path d="M24 80V64C14 58 9 48 9 37 9 19 22 6 40 6s31 12 31 28c0 4-1 7 2 12l-5 3v9c0 4-3 7-7 7h-6v15"/><circle cx="40" cy="32" r="3"/><path d="M40 20v4M40 40v4M28 32h4M48 32h4M32 24l3 3M45 37l3 3M48 24l-3 3M32 40l3-3"/></svg>
    <h3>DYSLEXIA</h3>
    <p>Lorem Ipsum is simply dummy text of the printing and typesetting industry. Lorem Ipsum has been the industry's standard dummy</p>
  </div>
  <div class="abs card" style="left:876px;top:73px">
    <svg width="80" height="84" viewBox="0 0 80 84" fill="none" stroke="#7c4dff" stroke-width="2.4" stroke-linejoin="round"><path d="M24 80V64C14 58 9 48 9 44 9 36 13 30 18 27M44 70h-6v10M46 60h4c4 0 6-3 6-6"/><circle cx="54" cy="26" r="22"/><circle cx="54" cy="26" r="14"/><circle cx="54" cy="26" r="6"/></svg>
    <h3>ADHD</h3>
    <p>Lorem Ipsum is simply dummy text of the printing and typesetting industry. Lorem Ipsum has been the industry's standard dummy</p>
  </div>
  <div class="abs card" style="left:372px;top:432px">
    <svg width="80" height="84" viewBox="0 0 80 84" fill="none" stroke="#7c4dff" stroke-width="2.4" stroke-linejoin="round"><path d="M40 30C30 22 26 18 26 12a7 7 0 0114-2 7 7 0 0114 2c0 6-4 10-14 18z"/><path d="M40 12v10M35 17h10"/><circle cx="22" cy="46" r="8"/><circle cx="58" cy="46" r="8"/><path d="M6 82V68c0-6 5-10 16-10s16 4 16 10v14M42 82V68c0-6 5-10 16-10s16 4 16 10v14"/></svg>
    <h3>COUPLES COUNSELING</h3>
    <p>Lorem Ipsum is simply dummy text of the printing and typesetting industry. Lorem Ipsum has been the industry's standard dummy</p>
  </div>
  <div class="abs card featured" style="left:623px;top:432px">
    <svg width="80" height="80" viewBox="0 0 80 80" fill="none" stroke="#fff" stroke-width="2.4" stroke-linejoin="round" stroke-linecap="round"><circle cx="32" cy="12" r="6"/><circle cx="50" cy="16" r="6"/><circle cx="40" cy="34" r="5"/><path d="M22 40c0-10 4-16 10-16s10 6 10 16M40 42c0-12 4-16 10-16s10 6 10 14M32 52c0-6 3-10 8-10s8 4 8 10"/><path d="M4 40c4 14 14 24 28 28l8 8 8-8c14-4 24-14 28-28"/></svg>
    <h3>MARRIAGE AND<br>FAMILY COUNSELING</h3>
    <p>Lorem Ipsum is simply dummy text of the printing and typesetting industry. Lorem Ipsum has been the industry's standard dummy</p>
  </div>
  <div class="abs card" style="left:876px;top:432px">
    <svg width="80" height="84" viewBox="0 0 80 84" fill="none" stroke="#7c4dff" stroke-width="2.4" stroke-linejoin="round"><circle cx="28" cy="12" r="8"/><circle cx="54" cy="12" r="8"/><path d="M16 80V34c0-8 4-12 12-12s12 4 12 12v46M40 80V36c0-10 5-14 14-14s14 4 14 14v16l-4 4v24"/><path d="M8 44l-2 36M28 40v40M54 50v30"/></svg>
    <h3>GERIATRICS</h3>
    <p>Lorem Ipsum is simply dummy text of the printing and typesetting industry. Lorem Ipsum has been the industry's standard dummy</p>
  </div>
</section>

<section class="chat">
  <div class="abs chat-photo" role="img" aria-label="Smiling family of four sitting on the floor in front of a sofa, parents forming a roof with their arms"></div>
  <h2 class="abs chat-title">HAVE A QUESTION? LET’S CHAT.</h2>
  <div class="abs rule" style="left:690px;top:96px;width:89px"></div>
  <p class="abs chat-copy">Lorem Ipsum is simply dummy text of the printing and typesetting industry.</p>
  <div class="abs field focus" style="left:690px;top:178px;width:213px">First Name</div>
  <div class="abs field" style="left:909px;top:178px;width:231px">Last Name</div>
  <div class="abs field" style="left:690px;top:234px;width:450px">Email address</div>
  <div class="abs field" style="left:690px;top:292px;width:213px">Phone Number</div>
  <div class="abs field" style="left:909px;top:292px;width:231px">Service</div>
  <div class="abs field area" style="left:690px;top:349px;width:450px">Message</div>
  <div class="abs btn btn-purple" style="left:690px;top:438px;width:148px;height:37px;font-size:12.5px">SUBMIT</div>
</section>

<footer class="site-footer">
  <h2 class="abs foot-title">CONTACT US</h2>
  <div class="abs foot-rule"></div>
  <div class="abs hq">HEADQUARTERS</div>
  <div class="abs hq-addr">Dummy Address is here,<br>City, Pincode-000 000</div>
  <div class="abs ico" style="left:344px;top:152px">
    <svg width="20" height="20" viewBox="0 0 24 24"><path d="M6.6 10.8c1.4 2.8 3.8 5.1 6.6 6.6l2.2-2.2c.3-.3.7-.4 1-.2 1.1.4 2.3.6 3.6.6.6 0 1 .4 1 1V20c0 .6-.4 1-1 1C10.6 21 3 13.4 3 4c0-.6.4-1 1-1h3.5c.6 0 1 .4 1 1 0 1.3.2 2.5.6 3.6.1.3 0 .7-.2 1z" fill="none" stroke="#fff" stroke-width="1.6"/></svg>
  </div>
  <div class="abs contact-line" style="top:157px">Call Us Today!<strong>1.888.888.888</strong></div>
  <div class="abs ico" style="left:344px;top:216px">
    <svg width="20" height="20" viewBox="0 0 24 24" fill="none" stroke="#fff" stroke-width="1.6" stroke-linejoin="round"><rect x="3" y="6" width="18" height="13" rx="1"/><path d="M3 7l9 7 9-7"/></svg>
  </div>
  <div class="abs contact-line" style="top:222px">Email Us<strong>info@k&amp;jcounseling.com</strong></div>
  <div class="abs foot-divider"></div>
  <div class="abs brand-foot">K &amp; J Counseling</div>
  <div class="abs foot-links">About us<span>|</span>Services<span>|</span>Contact us</div>
  <div class="abs copyright">K&amp;J Counseling © 2023 All Rights Reserved.</div>
</footer>

</body>
</html>
```